Extension to existing project

THIS IS A PROJECT FOR VALTRIK DESIGN. PLEASE DON'T BID FOR THIS PROJECT.

This project is an extension of a previous project to:
a) review the actual implementation of the design, and provide recommendations
b) fix/enhance/add any graphic assets that might be needed
c) create 'achievement' square icons

```html
<!DOCTYPE html>
<html lang="en">
<head>
<meta charset="utf-8">
<title>Top 100 Players</title>
<link rel="stylesheet" href="https://fonts.googleapis.com/css2?family=Sorts+Mill+Goudy&display=swap">
<style>
  :root {
    --wood-dark: #4a2410;
    --wood-mid: #8a4a22;
    --wood-light: #b8733b;
    --band: rgba(30, 12, 4, 0.72);
    --row: rgba(45, 18, 6, 0.62);
    --ink-light: #fbf1e2;
    --ink-soft: #e8d6bd;
    --paper: #f3e3c4;
    --paper-edge: #d9c19a;
    --paper-ink: #b08558;
    --paper-ink-deep: #9a6a3c;
    --field: #fbf5ea;
    --field-line: #c9a97e;
    --green: #2f8a1c;
    --green-dark: #1d5f10;
    --red: #b3120e;
    --red-dark: #6e0906;
    --gold: #f2c12e;
    --gold-dark: #b4820e;
  }
  * { box-sizing: border-box; margin: 0; padding: 0; }
  html, body { width: 1200px; height: 697px; overflow: hidden; background: #2a1408; }
  body { font-family: "Sorts Mill Goudy", Georgia, serif; color: var(--ink-light); }

  .screen { position: relative; width: 1200px; height: 697px; overflow: hidden; border-radius: 14px; }
  .wood {
    position: absolute; inset: 0;
    background:
      linear-gradient(120deg, rgba(0,0,0,0.35) 0%, transparent 30%, rgba(0,0,0,0.25) 55%, transparent 75%, rgba(0,0,0,0.35) 100%),
      linear-gradient(90deg, var(--wood-dark), var(--wood-mid) 25%, var(--wood-light) 50%, var(--wood-mid) 75%, var(--wood-dark));
  }

  .top-bar { position: absolute; left: 0; top: 0; width: 1200px; height: 96px; background: var(--band); }
  .title { position: absolute; top: 16px; width: 100%; text-align: center; font-size: 54px; font-weight: 400; color: var(--ink-light); text-shadow: 0 2px 4px rgba(0,0,0,.5); }
  .back-icon { position: absolute; left: 112px; top: 30px; }
  .refresh-icon { position: absolute; left: 1044px; top: 30px; }

  .col-head { position: absolute; top: 114px; font-size: 26px; line-height: 1; }
  .col-head small { display: block; font-size: 13px; color: var(--ink-soft); margin-top: 1px; }
  .coin { position: absolute; left: 952px; top: 114px; }

  .row { position: absolute; left: 190px; width: 820px; height: 46px; background: var(--row); }
  .row span { position: absolute; }
  .player { left: 38px; top: 4px; font-size: 22px; text-align: center; line-height: 1; }
  .player small, .level small, .rating small { display: block; font-size: 11px; color: var(--ink-soft); margin-top: 2px; }
  .level { left: 261px; top: 4px; font-size: 21px; line-height: 1; }
  .level small { text-align: left; }
  .rating { left: 588px; top: 4px; font-size: 21px; line-height: 1; }
  .prize { left: 752px; top: 11px; width: 60px; text-align: center; font-size: 21px; }

  .note { position: absolute; background: linear-gradient(160deg, #f7ead0, var(--paper) 60%, #ead5b0); box-shadow: 0 6px 14px rgba(0,0,0,.45); }
  .note .curl { position: absolute; }
  .info-note { left: 403px; top: 151px; width: 343px; height: 377px; }
  .info-title { position: absolute; top: 40px; width: 100%; text-align: center; font-size: 29px; line-height: 38px; color: var(--paper-ink); }
  .field { position: absolute; left: 57px; width: 264px; height: 42px; border: 1.5px solid var(--field-line); border-radius: 14px; background: var(--field); font-size: 21px; color: var(--paper-ink-deep); padding: 7px 18px; }
  .field.name { top: 141px; }
  .field.country { top: 203px; background: #f6ead3; }
  .field.country::after { content: "▼"; position: absolute; right: 18px; top: 11px; font-size: 13px; }

  .btn { position: absolute; display: flex; align-items: center; justify-content: center; text-align: center; color: var(--ink-light); border-radius: 4px; box-shadow: 0 2px 4px rgba(0,0,0,.5); }
  .btn-green { background: linear-gradient(var(--green), var(--green-dark)); }
  .btn-red { background: linear-gradient(var(--red), var(--red-dark)); }
  .ok-btn { left: 141px; top: 277px; width: 104px; height: 57px; font-size: 24px; }

  .cube-note { left: 604px; top: 391px; width: 566px; height: 165px; }
  .cube-title { position: absolute; top: 22px; width: 100%; text-align: center; font-size: 29px; color: var(--paper-ink-deep); }
  .cube-sub { position: absolute; top: 58px; width: 100%; text-align: center; font-size: 18px; color: var(--paper-ink-deep); }
  .take-btn { left: 133px; top: 102px; width: 83px; height: 41px; font-size: 18px; }
  .resign-btn { left: 350px; top: 102px; width: 83px; height: 41px; font-size: 18px; }

  .bottom-bar { position: absolute; left: 0; top: 616px; width: 1200px; height: 81px; background: var(--band); }
  .foot-btn { top: 14px; height: 54px; font-size: 18px; line-height: 21px; }
  .ratings-help { left: 115px; width: 234px; }
  .name-country { left: 487px; width: 234px; }
  .your-rating { left: 869px; width: 216px; font-size: 20px; gap: 10px; }
</style>
</head>
<body>
<div class="screen">
  <div class="wood" role="img" aria-label="Dark wooden board background with diagonal grain"></div>

  <header class="top-bar">
    <svg class="back-icon" width="44" height="36" viewBox="0 0 44 36" aria-label="Back">
      <path d="M20 2 L4 18 L20 34 M38 2 L22 18 L38 34" fill="none" stroke="#d8d0c4" stroke-width="7" stroke-linejoin="miter"/>
    </svg>
    <h1 class="title">Top 100 Players</h1>
    <svg class="refresh-icon" width="40" height="40" viewBox="0 0 40 40" aria-label="Refresh">
      <path d="M8 18 A12 12 0 0 1 30 12" fill="none" stroke="#d8d0c4" stroke-width="5"/>
      <path d="M26 6 L36 8 L32 18 Z" fill="#d8d0c4"/>
      <path d="M32 22 A12 12 0 0 1 10 28" fill="none" stroke="#d8d0c4" stroke-width="5"/>
      <path d="M14 34 L4 32 L8 22 Z" fill="#d8d0c4"/>
    </svg>
  </header>

  <div class="col-head" style="left:213px;"># Player<small style="margin-left:21px;">Country</small></div>
  <div class="col-head" style="left:434px;">Level<small>Achievements</small></div>
  <div class="col-head" style="left:758px;">Rating<small>Games Played</small></div>
  <svg class="coin" width="40" height="40" viewBox="0 0 40 40" aria-label="Prize">
    <circle cx="20" cy="20" r="19" fill="var(--gold-dark)"/>
    <circle cx="20" cy="20" r="16" fill="var(--gold)"/>
    <text x="20" y="28" text-anchor="middle" font-size="22" font-family="Georgia, serif" fill="var(--gold-dark)">$</text>
  </svg>

  <div class="leaderboard">
    <div class="row" style="top:170px;"><span class="player">1 Beaver<small>Norway</small></span><span class="level">World Grandmaster<small>69%</small></span><span class="rating">2331<small>2105</small></span><span class="prize">$195</span></div>
    <div class="row" style="top:223px;"><span class="player">1 Beaver<small>Norway</small></span><span class="level">World Grandmaster<small>69%</small></span><span class="rating">2331<small>2105</small></span><span class="prize">$195</span></div>
    <div class="row" style="top:276px;"><span class="player">1 Beaver<small>Norway</small></span><span class="level">World Grandmaster<small>69%</small></span><span class="rating">2331<small>2105</small></span><span class="prize">$195</span></div>
    <div class="row" style="top:329px;"><span class="player">1 Beaver<small>Norway</small></span><span class="level">World Grandmaster<small>69%</small></span><span class="rating">2331<small>2105</small></span><span class="prize">$195</span></div>
    <div class="row" style="top:382px;"><span class="player">1 Beaver<small>Norway</small></span><span class="level">World Grandmaster<small>69%</small></span><span class="rating">2331<small>2105</small></span><span class="prize">$195</span></div>
    <div class="row" style="top:435px;"><span class="player">1 Beaver<small>Norway</small></span><span class="level">World Grandmaster<small>69%</small></span><span class="rating">2331<small>2105</small></span><span class="prize">$195</span></div>
    <div class="row" style="top:488px;"><span class="player">1 Beaver<small>Norway</small></span><span class="level">World Grandmaster<small>69%</small></span><span class="rating">2331<small>2105</small></span><span class="prize">$195</span></div>
    <div class="row" style="top:541px;"><span class="player">1 Beaver<small>Norway</small></span><span class="level">World Grandmaster<small>69%</small></span><span class="rating">2331<small>2105</small></span><span class="prize">$195</span></div>
  </div>

  <section class="note info-note">
    <svg class="curl" style="left:-6px;top:-4px;" width="40" height="30" viewBox="0 0 40 30"><path d="M0 0 L40 4 L6 30 Z" fill="var(--paper-edge)"/></svg>
    <h2 class="info-title">Update your info<br>to share your rating</h2>
    <div class="field name">Your Name :</div>
    <div class="field country">Country or Region</div>
    <div class="btn btn-green ok-btn">Ok</div>
  </section>

  <section class="note cube-note">
    <svg class="curl" style="left:-8px;top:-6px;" width="46" height="30" viewBox="0 0 46 30"><path d="M0 0 L46 6 L8 30 Z" fill="var(--paper-edge)"/></svg>
    <svg class="curl" style="right:-8px;bottom:-8px;" width="40" height="34" viewBox="0 0 40 34"><path d="M40 34 L0 30 L34 0 Z" fill="var(--paper-edge)"/></svg>
    <h2 class="cube-title">The PC wants to double the cube.</h2>
    <p class="cube-sub">Do you Take ( Accept ) or Resign?</p>
    <div class="btn btn-green take-btn">Take</div>
    <div class="btn btn-red resign-btn">Resign</div>
  </section>

  <footer class="bottom-bar">
    <div class="btn btn-red foot-btn ratings-help">How are ratings<br>calculated?</div>
    <div class="btn btn-red foot-btn name-country">Your Name<br>&amp; Contry</div>
    <div class="btn btn-green foot-btn your-rating">
      <svg width="24" height="24" viewBox="0 0 24 24" aria-hidden="true"><path d="M12 1 L15 9 L23 9 L17 14 L19 22 L12 17 L5 22 L7 14 L1 9 L9 9 Z" fill="var(--ink-light)"/></svg>
      Your rating: 1000
    </div>
  </footer>
</div>
</body>
</html>
```